All About How Do Title Loans Work?*

Hi There,<br/>We: Bluefern Auto Pledge Lending (Loan agency in the US) are looking to get infographic design services for our most comprehensive guide: How do Title Loans Work. <br/>This guide has 6 steps that describe the title loan process/ service that we offer to our clients. <br/>If you’d like to know how car title loans work, then read this: https://bluefernlending.example/how-do-title-loans-work/

Target Market(s)

Personal Loans in US

Industry/Entity Type

Financial

Requirements
Must have
• Logo
• 1-6 steps
• Apply now + How Much Cash Can I Get https://snapvue.example/k8tzq1 / https://snapvue.example/k8tzw4 (call to action): Find that buttons here: https://bluefernlending.example/can-i-get-a-title-loan-if-the-title-is-not-in-my-name/
• The disclaimers: Please use the disclaimer that appears below the content: examples: https://snapvue.example/k8vb37 https://snapvue.example/k8vb5n https://snapvue.example/k8vb9d etc.
Nice to have
• Marisol: https://bluefernlending.example/apply-now/ (our presenter)-> https://snapvue.example/k8tyh2
Should not have
• Colors that not related to our website
• Don't promise anything we can't deliver (we have strict guidelines in the loan industry)

```html
<!DOCTYPE html>
<html lang="en">
<head>
<meta charset="utf-8">
<title>6 Simple Steps to Get Car Title Loans – Bluefern Auto Pledge Lending</title>
<link rel="stylesheet" href="https://fonts.googleapis.com/css2?family=Kanit:wght@400;500;600&display=swap">
<style>
  :root {
    --sun: #ffe155;
    --coral: #ee674a;
    --sky: #13a0ea;
    --ink: #454f5b;
    --dark: #1d1d1f;
    --white: #ffffff;
    --rule: #cfcfcf;
    --green: #7ac943;
    --skin: #f7d95b;
    --cash: #3aa6e8;
  }
  * { box-sizing: border-box; margin: 0; padding: 0; }
  html, body { width: 1200px; height: 1085px; overflow: hidden; }
  body { background: var(--sun); font-family: "Kanit", sans-serif; color: var(--ink); }
  .canvas { position: relative; width: 1200px; height: 1085px; background: var(--sun); }

  .header-band { position: absolute; left: 0; top: 0; width: 846px; height: 171px; background: var(--coral); }
  .brand-zone { position: absolute; left: 846px; top: 0; width: 354px; height: 171px; background: var(--white); }
  .title-number { position: absolute; left: 70px; top: 30px; font-size: 100px; font-weight: 600; color: var(--white); line-height: 1; }
  .title-text { position: absolute; left: 151px; top: 30px; font-size: 54px; font-weight: 600; color: var(--white); line-height: 58px; letter-spacing: 3px; text-transform: uppercase; }
  .hero-car { position: absolute; left: 656px; top: 99px; width: 236px; height: 97px; border-radius: 50px 60px 24px 24px; background: linear-gradient(#2aa9f0, #128fd6); }
  .brand-dot { position: absolute; left: 800px; top: 51px; width: 86px; height: 86px; border-radius: 50%; background: var(--coral); }
  .brand-name { position: absolute; left: 906px; top: 62px; width: 284px; font-size: 27px; font-weight: 600; line-height: 32px; color: var(--dark); }

  .card { position: absolute; left: 82px; width: 1054px; background: var(--white); border-radius: 32px; }
  .card-requirements { top: 192px; height: 412px; }
  .card-application { top: 628px; height: 354px; }
  .step-badge { position: absolute; left: -38px; top: 26px; width: 78px; height: 78px; border-radius: 50%; background: var(--sky); color: var(--white); font-size: 58px; font-weight: 500; display: flex; align-items: center; justify-content: center; }
  .step-title { position: absolute; left: 53px; top: 30px; font-size: 44px; font-weight: 600; color: var(--dark); letter-spacing: 0.5px; }

  .req-list { position: absolute; left: 0; top: 150px; width: 100%; height: 160px; list-style: none; }
  .req-item { position: absolute; top: 0; width: 160px; margin-left: -80px; text-align: center; }
  .req-icon { display: block; margin: 0 auto; height: 95px; }
  .req-icon.person { width: 92px; border-radius: 50%; background: var(--skin); }
  .req-icon.car { width: 112px; border-radius: 30px 30px 14px 14px; background: var(--sky); }
  .req-icon.title-card, .req-icon.id-card { width: 116px; height: 86px; margin: 4px auto 5px; border: 5px solid var(--ink); border-radius: 6px; }
  .req-icon.title-card { background: #eef3f8; }
  .req-icon.id-card { background: #e9f4fc; }
  .req-icon.cash { width: 92px; border-radius: 10px; background: var(--cash); }
  .req-icon.chat { width: 126px; border-radius: 46px; background: linear-gradient(90deg, var(--skin) 60%, var(--sky) 60%); }
  .req-label { display: block; margin-top: 14px; font-size: 26px; font-weight: 500; line-height: 28px; color: var(--ink); }
  .disclaimer { position: absolute; left: 62px; top: 336px; width: 908px; font-size: 13.5px; line-height: 18px; letter-spacing: 0.3px; text-align: center; color: var(--ink); }

  .ways-heading { position: absolute; right: 52px; top: 36px; font-size: 30px; font-weight: 500; letter-spacing: 1.5px; color: var(--ink); }
  .divider { position: absolute; top: 154px; width: 2px; height: 148px; background: var(--rule); }
  .option { position: absolute; text-align: center; }
  .option-label { font-size: 26px; font-weight: 500; color: var(--ink); }
  .opt-call { left: 0; top: 142px; width: 290px; }
  .phone-icon { display: block; margin: 0 auto; width: 44px; height: 44px; }
  .phone-number { display: block; margin-top: 6px; font-size: 30px; font-weight: 500; color: var(--sky); letter-spacing: 2.5px; }
  .opt-call .option-label { margin-top: 10px; }
  .opt-branch { left: 290px; top: 166px; width: 242px; }
  .branch-mark { display: block; font-size: 22px; font-weight: 500; line-height: 22px; color: var(--sky); text-transform: uppercase; }
  .opt-branch .option-label { margin-top: 34px; }
  .laptop-art { position: absolute; left: 583px; top: 132px; width: 101px; height: 107px; border-radius: 8px; background: linear-gradient(#f5f6f8 60%, var(--sky) 60%); }
  .online-steps { position: absolute; left: 713px; top: 146px; list-style: none; font-size: 17px; font-weight: 500; line-height: 23px; color: var(--ink); letter-spacing: 0.8px; }
  .online-label { position: absolute; left: 583px; top: 246px; width: 410px; text-align: center; font-size: 27px; font-weight: 500; color: var(--ink); letter-spacing: 1px; }
</style>
</head>
<body>
<main class="canvas">
  <header>
    <div class="header-band"></div>
    <div class="brand-zone"></div>
    <div class="title-number">6</div>
    <h1 class="title-text">Simple Steps to Get<br>Car Title Loans</h1>
    <div class="brand-dot"></div>
    <div class="hero-car" role="img" aria-label="Illustration of a blue car"></div>
    <div class="brand-name">Bluefern Auto Pledge Lending</div>
  </header>

  <section class="card card-requirements">
    <div class="step-badge">1</div>
    <h2 class="step-title">REQUIREMENTS</h2>
    <ul class="req-list">
      <li class="req-item" style="left:93px"><span class="req-icon person" role="img" aria-label="Illustration of a person in a suit"></span><span class="req-label">Personal<br>Details</span></li>
      <li class="req-item" style="left:261px"><span class="req-icon car" role="img" aria-label="Illustration of a car, front view"></span><span class="req-label">Car<br>Details</span></li>
      <li class="req-item" style="left:427px"><span class="req-icon title-card" role="img" aria-label="Illustration of a car title document"></span><span class="req-label">Car<br>Title</span></li>
      <li class="req-item" style="left:591px"><span class="req-icon id-card" role="img" aria-label="Illustration of an identity card"></span><span class="req-label">Identity</span></li>
      <li class="req-item" style="left:759px"><span class="req-icon cash" role="img" aria-label="Illustration of banknotes"></span><span class="req-label">Regular<br>Income</span></li>
      <li class="req-item" style="left:927px"><span class="req-icon chat" role="img" aria-label="Illustration of a person with a speech bubble"></span><span class="req-label">References</span></li>
    </ul>
    <p class="disclaimer">Disclaimer: There is a chance you'll need to show additional documents, according to your situation. When you finalize the loan details, be sure to inquire as to what is required, because it can vary according to your precise loan terms.</p>
  </section>

  <section class="card card-application">
    <div class="step-badge">2</div>
    <h2 class="step-title">APPLICATION</h2>
    <p class="ways-heading">3 Ways You Can Apply</p>

    <div class="option opt-call">
      <svg class="phone-icon" viewBox="0 0 24 24" aria-hidden="true"><path fill="#7ac943" d="M6.6 10.8c1.4 2.8 3.8 5.1 6.6 6.6l2.2-2.2c.3-.3.7-.4 1-.2 1.1.4 2.3.6 3.6.6.6 0 1 .4 1 1V20c0 .6-.4 1-1 1C10.6 21 3 13.4 3 4c0-.6.4-1 1-1h3.5c.6 0 1 .4 1 1 0 1.3.2 2.5.6 3.6.1.3 0 .7-.2 1L6.6 10.8z"/></svg>
      <span class="phone-number">(555) 014 2287</span>
      <p class="option-label">Call</p>
    </div>
    <div class="divider" style="left:289px"></div>

    <div class="option opt-branch">
      <span class="branch-mark">Visit<br>Branch</span>
      <p class="option-label">Visit Branch</p>
    </div>
    <div class="divider" style="left:531px"></div>

    <div class="laptop-art" role="img" aria-label="Illustration of a laptop with a checklist"></div>
    <ol class="online-steps">
      <li>1. Enter Your Car's Details</li>
      <li>2. Your Personal Information</li>
      <li>3. Address, Date of Birth and SSN</li>
      <li>4. Upload Photos of Your Vehicle</li>
    </ol>
    <p class="online-label">Apply Online in 4 easy steps</p>
  </section>
</main>
</body>
</html>
```